VELDORium - Awaken Your Inner Spark

I need PowerPoint presentation for my brand that is matching that attached briefing document. Please read the brief and specially the brand themes . I am looking for something impressive , Bold, eye catchy, strong visuals with less wording , advanced motion styling for the graphics and visuals

Please check the sample snapshot photos attached for a good direction of the design and bright and glorious color styles.

Here are some themes that are aligned with our brand, if you can use one or few or all of the below themes into consideration in the design.

- Unleash: Unleashing human true self is a breakthrough comparable to the Big Bang effect. It involves tapping into untapped capabilities, pushing boundaries, and experiencing transformative growth, expanding our true identity.

- Journey: The inward journey of change unravels the circles and layers of the human being, revealing the true core circle. It is a quest to discover our authentic essence, untouched by external influences, and embrace the depth of our being.

- Stained glass: The stained glass mirrors the complexities of our existence, with its fragments and imperfections. Through the light, it forms a captivating mosaic, reminding us that we are not defined by our past. Even in brokenness, beauty and meaning can be found.

- Chisel: The chisel symbolizes embracing our potential to become our true selves. In the hands of the sculptor chipping away at excess stone, we shed wrong beliefs , fears, and limitations Through this process, we uncover our authentic selves and live in alignment with our true purpose.

Target Market(s)

International

Industry/Entity Type

Community Services

Requirements
Must have
• Bold style and royal and powerful colours
Nice to have
• Motion slides
Should not have
• please do not use Corporate companies style presentations

```html
<!DOCTYPE html>
<html lang="en">
<head>
<meta charset="utf-8">
<title>VELDORium - Awaken Your Inner Spark</title>
<link rel="stylesheet" href="https://fonts.googleapis.com/css2?family=Roboto:wght@400;500;700;900&family=Noto+Sans+Arabic:wght@400;500&display=swap">
<style>
:root{
  --gold:#b3872c;
  --gold-deep:#9a7222;
  --gold-pale:#e8dcc2;
  --ink:#161616;
  --body:#383838;
  --page:#575757;
  --white:#ffffff;
  --warm:#f8efe2;
}
*{margin:0;padding:0;box-sizing:border-box}
html,body{width:1200px;height:3981px;overflow:hidden;background:var(--page)}
body{position:relative;font-family:"Roboto",Arial,sans-serif;color:var(--ink)}
.slide{position:absolute;left:46px;width:1106px;height:620px;overflow:hidden;
  background:
    radial-gradient(ellipse 55% 60% at 50% 50%,rgba(255,255,255,.95) 0%,rgba(255,255,255,0) 70%),
    radial-gradient(ellipse at 20% 90%,rgba(214,205,236,.55) 0%,rgba(214,205,236,0) 55%),
    radial-gradient(ellipse at 85% 15%,rgba(236,214,224,.45) 0%,rgba(236,214,224,0) 55%),
    linear-gradient(180deg,#e6e5ee 0%,#eceaf1 50%,#e1dfea 100%)}
.abs{position:absolute}
.footer-mark{position:absolute;left:54px;bottom:20px;font-size:13px;color:var(--gold);font-style:italic}
.title{position:absolute;left:0;width:100%;text-align:center;font-weight:700;font-size:31px;letter-spacing:.2px}
.title .accent{color:var(--gold)}
.underline{position:absolute;height:3px;background:var(--gold)}
.photo{position:absolute}
.ring{position:absolute;border-radius:50%;background:var(--white);display:flex;align-items:center;justify-content:center}

/* cover */
.cover{background:
    radial-gradient(circle at 50% 72%,rgba(255,244,214,1) 0%,rgba(255,236,196,.75) 10%,rgba(255,255,255,0) 38%),
    radial-gradient(ellipse 70% 60% at 50% 55%,rgba(255,255,255,.9) 0%,rgba(255,255,255,0) 70%),
    linear-gradient(180deg,#dcdbe7 0%,#e9e7ef 45%,#e6e2e6 75%,#d9d7e3 100%)}
.cover .brand{top:198px;font-size:66px;font-weight:500;letter-spacing:.5px}
.cover .arabic{top:296px;left:0;width:100%;text-align:center;font-family:"Noto Sans Arabic",sans-serif;font-size:30px}
.cover .tagline{top:372px;left:0;width:100%;text-align:center;font-size:32px}

/* challenges */
.challenges{background:linear-gradient(180deg,#ffffff 0%,#fbfbfc 100%)}
.challenges .title{left:54px;width:auto;text-align:left;top:42px;font-size:32px}
.challenges .body{position:absolute;left:54px;top:105px;width:518px;font-size:13.4px;line-height:27px;color:var(--body)}
.challenges .body b{color:var(--ink);font-weight:500}
.challenges .bar{position:absolute;left:612px;top:0;width:17px;height:620px;background:var(--gold)}

/* needs */
.needs .intro{position:absolute;left:150px;width:806px;top:80px;text-align:center;font-size:13px;line-height:27px;color:var(--body)}
.needs .intro b{color:var(--ink);font-weight:500}
.need{position:absolute;top:140px;width:232px;text-align:center}
.need .ring{position:relative;margin:0 auto;width:152px;height:152px;background:var(--gold);
  border:7px solid var(--gold-pale);box-shadow:0 6px 14px rgba(90,60,10,.25)}
.need .ring::after{content:"";position:absolute;inset:6px;border-radius:50%;border:2px solid rgba(255,255,255,.85)}
.need h3{margin-top:22px;font-size:17px;font-weight:700}
.need p{margin-top:8px;font-size:11px;line-height:23px;color:var(--body)}
.needs .band{position:absolute;left:161px;top:492px;width:784px;height:88px;background:var(--gold);color:var(--white);
  font-size:13px;line-height:23px;text-align:center;display:flex;align-items:center;justify-content:center;padding:0 54px}
.needs .band b{font-weight:700}

/* what */
.what h3{position:absolute;font-size:17px;font-weight:700}
.what p{position:absolute;font-size:14px;line-height:29px;color:var(--body)}
.what .ring{border:9px solid var(--gold);box-shadow:0 6px 14px rgba(90,60,10,.25)}

/* how */
.svc{position:absolute;width:232px}
.svc h4{font-size:14px;font-weight:700}
.svc p{font-size:13px;line-height:21px;color:var(--body);margin-top:5px}
.svc-icon{position:absolute;width:88px;height:88px;border-radius:50%;background:var(--white);border:6px solid var(--gold);
  display:flex;align-items:center;justify-content:center;box-shadow:0 4px 10px rgba(90,60,10,.2)}
.hub{position:absolute;left:422px;top:115px;width:270px;height:270px;border-radius:50%;background:#d8c7a3;
  display:flex;align-items:center;justify-content:center}
.hub-inner{width:232px;height:232px;border-radius:50%;background:#fbf6ec;border:14px solid var(--gold);
  display:flex;align-items:center;justify-content:center;text-align:center;font-weight:700;font-size:22px;line-height:32px;
  box-shadow:0 4px 12px rgba(90,60,10,.3)}
.info-box{position:absolute;top:427px;width:471px;height:157px;border:2px solid var(--gold);background:rgba(255,255,255,.4);text-align:center;padding:14px 12px}
.info-box h4{font-size:14px;font-weight:700}
.info-box p{font-size:10.6px;line-height:23px;color:var(--body);margin-top:8px}

/* contact */
.contact{background:
    radial-gradient(circle at 50% 0%,rgba(255,230,180,.9) 0%,rgba(255,240,214,.5) 25%,rgba(255,255,255,0) 55%),
    linear-gradient(180deg,#faf1e3 0%,var(--warm) 50%,#f4ebe2 100%)}
.contact .brand{top:208px;font-size:46px;font-weight:900}
.contact .touch{top:285px;left:0;width:100%;text-align:center;font-size:31px;position:absolute}
.contact-item{position:absolute;top:349px;display:flex;align-items:center;gap:18px;font-size:18px}
.contact-item .dot{width:58px;height:58px;border-radius:50%;background:var(--gold);display:flex;align-items:center;justify-content:center}
</style>
</head>
<body>

<!-- Cover -->
<section class="slide cover" style="top:42px">
  <div class="title brand">VELDORium.com</div>
  <div class="abs arabic" dir="rtl">دعوة للفرد لكي يكون انسان ويكون نفسه</div>
  <div class="abs tagline">Awaken Your Inner Spark</div>
</section>

<!-- Life challenges -->
<section class="slide challenges" style="top:697px">
  <h2 class="title">Life challenges <span class="accent">in UAE</span></h2>
  <div class="underline" style="left:54px;top:90px;width:66px"></div>
  <div class="body">
    The paradox between the quality of life in the UAE and the prevalence of mental health problems is a significant concern. On one hand, the UAE is known for its luxurious lifestyle, economic prosperity, and modern infrastructure, contributing to a high overall standard of living. However, local studies have revealed notable rise in mental health disorders within the population where the prevalence rate for anxiety was the highest at 56%, followed by depression, post-traumatic disorders,<br>
    Factors contributing to this paradox include the fast-paced and competitive nature of the society, high work demands, increased stress levels, and social isolation. The pressure to succeed, maintain a certain image, and meet societal expectations can take a toll on individuals' mental well-being, despite the outward appearance of prosperity. Addressing this paradox requires a comprehensive approach that focuses on <b>Encouraging individuals living in UAE to cultivate their humanity and be true to themselves.</b><br>
    By recognizing the importance of <b>Authentic Self, Human Essence and True</b> Identity, the UAE can work towards bridging the gap between its high quality of life and the prevalence of mental health disorders.
  </div>
  <div class="bar"></div>
  <div class="photo" role="img" aria-label="Night city skyline across the water with a mosque lit in colourful stained-glass light" style="left:629px;top:0;width:477px;height:620px;background:
    radial-gradient(ellipse 60% 22% at 45% 82%,rgba(70,160,220,.85) 0%,rgba(70,160,220,0) 70%),
    radial-gradient(ellipse 40% 16% at 70% 78%,rgba(200,70,170,.7) 0%,rgba(200,70,170,0) 70%),
    radial-gradient(ellipse 30% 14% at 25% 74%,rgba(240,170,60,.75) 0%,rgba(240,170,60,0) 70%),
    linear-gradient(180deg,#3a4766 0%,#5d5870 22%,#c48a4e 36%,#7a5a58 44%,#2f3a55 55%,#1e2c44 75%,#141a28 100%)"></div>
  <div class="ring" style="left:761px;top:203px;width:212px;height:212px;box-shadow:0 8px 20px rgba(0,0,0,.35)">
    <div class="ring" style="position:relative;width:172px;height:172px;background:var(--gold)">
      <svg width="104" height="104" viewBox="0 0 100 100" fill="none" stroke="#fff" stroke-width="4" stroke-linejoin="round" stroke-linecap="round">
        <path d="M12 88h16V72h16V56h16V40"/>
        <path d="M56 88h32V50"/>
        <circle cx="72" cy="28" r="12"/><circle cx="72" cy="28" r="4"/>
        <path d="M72 10v4M72 42v4M54 28h4M86 28h4"/>
        <circle cx="30" cy="24" r="6"/><path d="M30 30v16M30 36l12-4M30 46l-6 12M30 46l8 10"/>
      </svg>
    </div>
  </div>
  <div class="footer-mark">VELDORium.com</div>
</section>

<!-- Human needs -->
<section class="slide needs" style="top:1353px">
  <h2 class="title" style="top:30px">Our Human <span class="accent">needs</span></h2>
  <div class="intro">At the core of human existence are fundamental needs for <b>identity, belonging, purpose, and impact.</b> These needs shape our perceptions, motivations, and overall well-being, playing a significant role in our journey towards personal fulfilment.</div>

  <svg class="abs" style="left:0;top:0" width="1106" height="620" fill="none" stroke="#111" stroke-width="3.5" stroke-linecap="round">
    <path d="M240 240 Q292 236 326 214"/><path d="M310 208l22 0-10 18" fill="#111"/>
    <path d="M498 198 Q560 192 590 230"/><path d="M578 214l16 22-22-4z" fill="#111"/>
    <path d="M753 240 Q806 236 836 214"/><path d="M820 208l22 0-10 18" fill="#111"/>
  </svg>

  <div class="need" style="left:50px">
    <div class="ring"><svg width="78" height="78" viewBox="0 0 80 80" fill="none" stroke="#fff" stroke-width="3"><rect x="14" y="10" width="36" height="52" rx="4"/><circle cx="32" cy="26" r="6"/><path d="M22 42h20M22 50h12"/><circle cx="56" cy="56" r="14" fill="#b3872c"/><path d="M49 56l5 5 9-9"/></svg></div>
    <h3>Identity</h3>
    <p>is the complex fabric that shapes our individuality, comprising our values, beliefs, culture, and personal experiences. A strong sense of identity allows us to embrace our uniqueness, navigate confidently, and form meaningful connections with others.</p>
  </div>
  <div class="need" style="left:306px">
    <div class="ring"><svg width="78" height="78" viewBox="0 0 80 80" fill="none" stroke="#fff" stroke-width="3" stroke-linejoin="round"><path d="M8 38L40 10l32 28M16 32v36h48V32"/><circle cx="40" cy="44" r="6"/><path d="M30 66v-8a10 10 0 0 1 20 0v8"/><circle cx="22" cy="58" r="4"/><circle cx="58" cy="58" r="4"/></svg></div>
    <h3>Belonging</h3>
    <p>is a deep human need to connect with others and be part of something greater. Through belonging, we form deep connections, and build enriching relationships that offer acceptance, understanding, and a shared sense of purpose.</p>
  </div>
  <div class="need" style="left:563px">
    <div class="ring"><svg width="78" height="78" viewBox="0 0 80 80" fill="none" stroke="#fff" stroke-width="3"><circle cx="38" cy="42" r="28"/><circle cx="38" cy="42" r="18"/><circle cx="38" cy="42" r="8"/><path d="M38 42L66 14M58 12h10v10"/></svg></div>
    <h3>Purpose</h3>
    <p>is the beacon that gives meaning to our actions and drives us towards fulfilment. It stems from understanding our goals, values, and passions, propelling us with direction and a sense of purpose. When our actions our purpose, we experience profound fulfilment.</p>
  </div>
  <div class="need" style="left:820px">
    <div class="ring"><svg width="78" height="78" viewBox="0 0 80 80" fill="none" stroke="#fff" stroke-width="3"><circle cx="40" cy="40" r="10"/><circle cx="18" cy="18" r="8"/><circle cx="62" cy="18" r="8"/><circle cx="18" cy="62" r="8"/><circle cx="62" cy="62" r="8"/><path d="M24 24l8 8M56 24l-8 8M24 56l8-8M56 56l-8-8"/></svg></div>
    <h3>Impact</h3>
    <p>is the intrinsic longing to create a significant and positive impact on others and society as a whole. Through our actions, words, and contributions, we have the power to influence, inspire, and leave a lasting legacy for future generations.</p>
  </div>

  <div class="band"><span>By acknowledging and nurturing these fundamental needs of <b>identity, belonging, purpose, and impact</b>, we embark on a transformative journey towards personal growth and fulfilment.</span></div>
  <div class="footer-mark">VELDORium.com</div>
</section>

<!-- The What -->
<section class="slide what" style="top:2008px">
  <h2 class="title" style="top:22px">The <span class="accent">What</span></h2>
  <div class="photo" role="img" aria-label="Waterfront resort with palm trees, a red bridge and a sail-shaped tower" style="left:54px;top:80px;width:490px;height:245px;background:
    radial-gradient(ellipse 40% 30% at 35% 65%,rgba(190,70,40,.7) 0%,rgba(190,70,40,0) 70%),
    linear-gradient(180deg,#7fb0e0 0%,#b9d0e4 30%,#d8b888 48%,#6c8a3e 66%,#3d5a3a 80%,#2f5868 100%)"></div>
  <div class="ring" style="left:484px;top:145px;width:120px;height:120px">
    <svg width="62" height="62" viewBox="0 0 60 60" fill="none" stroke="#111" stroke-width="3"><circle cx="28" cy="32" r="20"/><circle cx="28" cy="32" r="11"/><circle cx="28" cy="32" r="3"/><path d="M28 32L50 10M44 8h8v8"/></svg>
  </div>
  <h3 style="left:618px;top:118px">Our Vision</h3>
  <p style="left:618px;top:152px;width:420px">Our vision is to provide a community platform that embraces the fundamental needs of identity, belonging, purpose, and impact, empowering individuals to discover their true identities, forge deep connections, and create a meaningful impact in the world.</p>

  <h3 style="left:54px;top:376px">Our Mission</h3>
  <p style="left:54px;top:410px;width:440px">Our mission is to cultivate a community services platform that fosters self-discovery, authentic connections, and purpose-driven actions. Through our platform, we aim to facilitate meaningful interactions, provide encourage individuals By fostering a sense of belonging, promoting personal development, and celebrating diverse perspectives.</p>
  <div class="photo" role="img" aria-label="Sandstone palace hotel on a turquoise lagoon with palms and a sail-shaped tower behind" style="left:561px;top:340px;width:489px;height:244px;background:
    linear-gradient(180deg,#9cc4ea 0%,#c9d7e4 22%,#c99a6a 42%,#a86d45 58%,#4f7a4c 72%,#5fb4a6 86%,#86cbbb 100%)"></div>
  <div class="ring" style="left:502px;top:403px;width:120px;height:120px">
    <svg width="62" height="62" viewBox="0 0 60 60" fill="none" stroke="#111" stroke-width="3"><rect x="8" y="6" width="32" height="46" rx="3"/><path d="M15 18h18M15 26h18M15 34h10"/><circle cx="44" cy="42" r="10" fill="#fff"/><circle cx="44" cy="42" r="4"/></svg>
  </div>
  <div class="footer-mark">VELDORium.com</div>
</section>

<!-- The How -->
<section class="slide how" style="top:2664px">
  <h2 class="title" style="top:38px">The How <span class="accent">VELDORium services</span></h2>
  <div class="underline" style="left:520px;top:84px;width:66px"></div>

  <div class="svc" style="left:92px;top:126px"><h4>Master Class</h4><p>Key topic from a subject matter expert speaker</p></div>
  <div class="svc" style="left:92px;top:230px"><h4>Workshops</h4><p>Intractive workshop for individuals</p></div>
  <div class="svc" style="left:92px;top:334px"><h4>Community Meetups</h4><p>Volunteer activities to Serve the city</p></div>
  <div class="svc" style="left:797px;top:126px"><h4>Group Support</h4><p>Small Circle Private Support Group</p></div>
  <div class="svc" style="left:797px;top:230px"><h4>Caregivers</h4><p>Private One to One Care</p></div>
  <div class="svc" style="left:797px;top:334px"><h4>Volunteer Services</h4><p>Volunteer activities to Serve the city</p></div>

  <div class="svc-icon" style="left:331px;top:104px"><svg width="44" height="44" viewBox="0 0 44 44" fill="none" stroke="#111" stroke-width="2.5"><rect x="12" y="4" width="28" height="20"/><path d="M18 11h16M18 17h10"/><circle cx="12" cy="30" r="5"/><path d="M4 42v-4a8 8 0 0 1 16 0v4M20 34h18"/></svg></div>
  <div class="svc-icon" style="left:331px;top:207px"><svg width="44" height="44" viewBox="0 0 44 44" fill="none" stroke="#111" stroke-width="2.5"><rect x="4" y="6" width="36" height="22"/><circle cx="14" cy="34" r="4"/><circle cx="30" cy="34" r="4"/><path d="M10 14h10M26 12v10"/></svg></div>
  <div class="svc-icon" style="left:331px;top:310px"><svg width="44" height="44" viewBox="0 0 44 44" fill="none" stroke="#111" stroke-width="2.5"><circle cx="22" cy="22" r="5"/><circle cx="8" cy="8" r="4"/><circle cx="36" cy="8" r="4"/><circle cx="8" cy="36" r="4"/><circle cx="36" cy="36" r="4"/><path d="M11 11l7 7M33 11l-7 7M11 33l7-7M33 33l-7-7"/></svg></div>
  <div class="svc-icon" style="left:692px;top:104px"><svg width="44" height="44" viewBox="0 0 44 44" fill="none" stroke="#111" stroke-width="2.5"><circle cx="22" cy="14" r="6"/><circle cx="8" cy="28" r="4"/><circle cx="36" cy="28" r="4"/><path d="M12 40a10 10 0 0 1 20 0M4 40a4 4 0 0 1 8 0M32 40a4 4 0 0 1 8 0"/></svg></div>
  <div class="svc-icon" style="left:692px;top:207px"><svg width="44" height="44" viewBox="0 0 44 44" fill="none" stroke="#111" stroke-width="2.5"><circle cx="22" cy="14" r="6"/><path d="M4 20l8 16h20l8-16M14 36v6M30 36v6"/></svg></div>
  <div class="svc-icon" style="left:692px;top:310px"><svg width="44" height="44" viewBox="0 0 44 44" fill="none" stroke="#111" stroke-width="2.5"><circle cx="22" cy="22" r="18"/><path d="M16 30v-12M20 30V12M24 30V12M28 30V18"/></svg></div>

  <div class="hub"><div class="hub-inner">VELDORium<br>Platform</div></div>

  <div class="info-box" style="left:75px">
    <h4>Masterclass</h4>
    <p>VELDORium will offer masterclass events where experts in a specific field from around the world will share their knowledge and skills through in person event. Learners will gain access to high-quality instruction from accomplished professionals, gaining valuable insights and practical guidance to enhance their own abilities.</p>
  </div>
  <div class="info-box" style="left:562px">
    <h4>Workshops</h4>
    <p>VELDORium will offer hands-on workshops in an interactive learning experience where participants actively engage in practical activities to gain practical skills and knowledge in a specific subject. It emphasizes experiential learning and provides a dynamic environment for participants to apply theory in practice.</p>
  </div>
  <div class="footer-mark">VELDORium.com</div>
</section>

<!-- Contact -->
<section class="slide contact" style="top:3321px">
  <div class="title brand">VELDORium.com</div>
  <div class="touch">Get In Touch</div>
  <div class="contact-item" style="left:93px">
    <span class="dot"><svg width="26" height="26" viewBox="0 0 24 24" fill="#fff"><path d="M6.6 10.8a15 15 0 0 0 6.6 6.6l2.2-2.2a1 1 0 0 1 1-.25 11.4 11.4 0 0 0 3.6.57 1 1 0 0 1 1 1V20a1 1 0 0 1-1 1A17 17 0 0 1 3 4a1 1 0 0 1 1-1h3.5a1 1 0 0 1 1 1c0 1.25.2 2.45.57 3.6a1 1 0 0 1-.25 1z"/></svg></span>
    <span>+1 555 0142 7788</span>
  </div>
  <div class="contact-item" style="left:416px">
    <span class="dot"><svg width="26" height="20" viewBox="0 0 26 20"><rect x="1" y="1" width="24" height="18" rx="2" fill="#fff"/><path d="M2 3l11 8 11-8" fill="none" stroke="#b3872c" stroke-width="2"/></svg></span>
    <span>info@veldorium.com</span>
  </div>
  <div class="contact-item" style="left:736px">
    <span class="dot"><svg width="24" height="26" viewBox="0 0 24 24" fill="#fff"><path d="M12 2a7 7 0 0 0-7 7c0 5 7 13 7 13s7-8 7-13a7 7 0 0 0-7-7zm0 9.5A2.5 2.5 0 1 1 12 6.5a2.5 2.5 0 0 1 0 5z"/></svg></span>
    <span>Veldor Lane, Northbrook</span>
  </div>
</section>

</body>
</html>
```